Stationery Required - Own Logo provided

Hi,

We are a retail company called 'Copperfinch Trading Limited' based in the UK and would like some corporate stationery designed.

We have provided our Logo which we would like to use (Its attached to this brief)...

The designs must be orginal, professional, stylish and interesting!

Target Market(s)

We will use this stationery to communicate with our wholesale suppliers and employees, so it must have a 'professional' feel about it.

Industry/Entity Type

It Company

Requirements
Must have
• Must be professional, corporate, stylish and not to 'fussy'. we require ... Business card design, a4 letter, compliment slip. All designs must be supplied in a format where the text (address/telephone numbers etc..) can be edited, as we have alot of staff and operate out of several different premises.
Nice to have
• I would like a windows backround picture file supplied as well so we can integrate that onto our computer systems.

```html
<!DOCTYPE html>
<html lang="en">
<head>
<meta charset="utf-8">
<title>Copperfinch Trading Limited – Business Card</title>
<link rel="stylesheet" href="https://fonts.googleapis.com/css2?family=Arimo:ital,wght@0,400;0,700;1,400&display=swap">
<style>
  :root {
    --brand-dark: #3b5a25;
    --brand-lime: #8cc63f;
    --wood-dark: #4a2418;
    --wood-mid: #6b3a2a;
    --grass: #a9c65a;
    --grass-light: #c4d88a;
    --pale: #e3ecc6;
    --paper: #ffffff;
    --ink: #3b5a25;
  }
  html, body {
    margin: 0;
    padding: 0;
    overflow: hidden;
    background: var(--paper);
  }
  .card {
    position: relative;
    width: 1200px;
    height: 669px;
    overflow: hidden;
    background: var(--paper);
    font-family: "Arimo", Arial, sans-serif;
    color: var(--ink);
  }
  .brand {
    position: absolute;
    left: 26px;
    top: 30px;
    display: flex;
    align-items: center;
    gap: 34px;
  }
  .brand-square {
    width: 200px;
    height: 200px;
    background: var(--brand-lime);
  }
  .brand-name {
    margin: 0;
    font-weight: 400;
    color: var(--brand-dark);
    line-height: 1;
  }
  .brand-name .line-main {
    display: block;
    font-size: 104px;
    letter-spacing: -2px;
  }
  .brand-name .line-sub {
    display: block;
    margin-top: 18px;
    font-size: 54px;
    letter-spacing: 62px;
  }
  .band {
    position: absolute;
    left: 0;
    width: 100%;
  }
  .band-wood-top {
    top: 260px;
    height: 40px;
    background: linear-gradient(180deg, var(--wood-mid) 0%, var(--wood-dark) 45%, var(--wood-mid) 70%, var(--wood-dark) 100%);
  }
  .band-grass-top {
    top: 300px;
    height: 54px;
    background: linear-gradient(180deg, var(--grass) 0%, var(--grass-light) 50%, var(--grass) 100%);
  }
  .band-pale {
    top: 354px;
    height: 217px;
    background: linear-gradient(180deg, #d8e5ad 0%, var(--pale) 30%, var(--pale) 70%, #d8e5ad 100%);
  }
  .band-grass-bottom {
    top: 571px;
    height: 52px;
    background: linear-gradient(180deg, var(--grass) 0%, var(--grass-light) 50%, var(--grass) 100%);
  }
  .band-wood-bottom {
    top: 623px;
    height: 46px;
    background: linear-gradient(180deg, var(--wood-dark) 0%, var(--wood-mid) 40%, var(--wood-dark) 75%, var(--wood-mid) 100%);
  }
  .lift {
    text-shadow: 2px 2px 0 #ffffff;
  }
  .person {
    position: absolute;
    left: 92px;
    top: 412px;
  }
  .person-name {
    margin: 0;
    font-size: 42px;
    font-weight: 400;
    line-height: 1;
  }
  .person-role {
    margin: 12px 0 0 -23px;
    font-size: 34px;
    font-style: italic;
    line-height: 1;
  }
  .contact {
    position: absolute;
    right: 16px;
    top: 374px;
    margin: 0;
    text-align: right;
    font-size: 34px;
    font-style: normal;
    line-height: 51px;
  }
  .contact b {
    font-weight: 700;
  }
</style>
</head>
<body>
  <div class="card">
    <header class="brand">
      <div class="brand-square" aria-hidden="true"></div>
      <h1 class="brand-name">
        <span class="line-main">Copperfinch Trading</span>
        <span class="line-sub">LIMITED</span>
      </h1>
    </header>

    <div class="band band-wood-top"></div>
    <div class="band band-grass-top"></div>
    <div class="band band-pale"></div>
    <div class="band band-grass-bottom"></div>
    <div class="band band-wood-bottom"></div>

    <section class="person lift">
      <p class="person-name">Rowan Keller</p>
      <p class="person-role">Company Director</p>
    </section>

    <address class="contact lift">
      <b>T.</b> 07700900461<br>
      <b>@.</b> hello@copperfinch.co.uk<br>
      <b>A.</b> 18 Harbour Row, Carrowmore,<br>
      County Down BT99 4XZ
    </address>
  </div>
</body>
</html>
```